Quarry Provision Partners needs a cool web design

We need a web design for a new start up called Quarry Provision Partners. QPP is all about working with mine sites to reduce costs and make their supply chains more effective and cost efficient. I have attached our logo and a very basic tile format layout for the website but I will take your advice on best layout. I do prefer a tile based page similar to "Farvenbrook.com/advisory" this displays a professional yet cool look. The secondary pages need to have the same format.
Target Market(s)
Target customers are typically men in the mining industry. They want simplicity and are time poor.
Industry/Entity Type
Mining
Coding
Coded - Design and coding required
Font styles to use
Requirements
Must have
- Must be simple, prefer tile based such as the Farvenbrooks.com/advisory website.
Use bold writing and fonts. No flowery fonts.
Must use corporate colors but don't make too dark.
the site must have connections to well designed second pages.

```html
<!DOCTYPE html>
<html lang="en">
<head>
<meta charset="utf-8">
<title>Quarry Provision Partners – Procurement Services</title>
<link rel="stylesheet" href="https://fonts.googleapis.com/css2?family=Bebas+Neue&family=Open+Sans:wght@400;600;700&display=swap">
<style>
  :root {
    --page-bg: #5b5b5b;
    --brand-red: #a2141b;
    --accent-orange: #f5a71c;
    --white: #ffffff;
    --text-dark: #1e1e1e;
    --text-grey: #6d6d6d;
    --rule-pink: #e3a3a3;
    --footer-grey: #c9c9c9;
  }
  * { margin: 0; padding: 0; box-sizing: border-box; }
  html, body { width: 1200px; height: 1000px; overflow: hidden; }
  body {
    background: var(--page-bg);
    font-family: "Open Sans", Arial, sans-serif;
    position: relative;
  }
  .brand {
    position: absolute; left: 0; top: 56px; width: 1200px;
    display: flex; justify-content: center; align-items: center; gap: 12px;
  }
  .brand-mark { width: 26px; height: 26px; background: var(--brand-red); }
  .brand-name {
    font-family: "Open Sans", sans-serif; font-weight: 600;
    color: var(--white); font-size: 24px; line-height: 30px;
  }
  .utility-icons { position: absolute; left: 87px; top: 126px; display: flex; gap: 18px; }
  .search {
    position: absolute; left: 962px; top: 123px; width: 124px; height: 22px;
    border: 1px solid #8a8a8a; background: #5e5e5e;
  }
  .search-icon { position: absolute; left: 1093px; top: 127px; }

  .hero { position: absolute; left: 85px; top: 153px; width: 1027px; height: 257px; display: flex; }
  .service-nav {
    width: 283px; height: 100%;
    background: linear-gradient(160deg, #3a2f29 0%, #2a221e 55%, #4a3a30 100%);
    padding-top: 8px;
  }
  .service-nav li {
    list-style: none; height: 40px; display: flex; align-items: center;
    padding-left: 10px; gap: 9px;
    color: var(--white); font-weight: 600; font-size: 14px;
  }
  .service-nav li::before {
    content: ""; width: 11px; height: 6px; background: var(--accent-orange);
    transform: skewX(-30deg);
  }
  .service-nav li.active { color: var(--accent-orange); }
  .hero-photo {
    flex: 1;
    background: radial-gradient(ellipse at 45% 55%, #7a4a30 0%, #3c2a22 40%, #0d0b0b 80%);
  }

  .content {
    position: absolute; left: 86px; top: 410px; width: 1026px; height: 502px;
    background: var(--white);
  }
  .page-head {
    height: 46px; border-bottom: 1px solid var(--rule-pink);
    position: relative;
  }
  .page-title {
    position: absolute; left: 82px; top: 10px;
    font-family: "Bebas Neue", sans-serif; font-size: 27px; color: var(--brand-red);
    font-weight: 400; line-height: 30px;
  }
  .breadcrumb {
    position: absolute; right: 14px; top: 17px;
    font-family: Arial, sans-serif; font-size: 10px; color: var(--text-grey); letter-spacing: 0.6px;
  }
  .page-body { display: flex; height: 430px; }
  .side-photo {
    width: 282px; height: 100%;
    background: linear-gradient(90deg, #dfeaf3 0%, #bcd2e4 30%, #1c1c1e 45%, #121213 85%, #d8e4ee 100%);
  }
  .copy { flex: 1; padding: 11px 28px 0 19px; }
  .copy p {
    font-family: Arial, sans-serif; font-size: 11.8px; line-height: 18px;
    color: var(--text-dark); letter-spacing: 0.95px; text-align: justify;
    margin-bottom: 18px;
  }
  .site-footer {
    position: absolute; left: 0; top: 476px; width: 100%; height: 26px;
    border-top: 1px solid var(--rule-pink);
    text-align: center; font-family: Arial, sans-serif; font-size: 12.5px;
    color: var(--text-dark); letter-spacing: 0.6px; padding-top: 5px;
  }
  .copyright {
    position: absolute; left: 87px; top: 928px;
    font-family: Arial, sans-serif; font-size: 9px; font-weight: 700;
    color: var(--footer-grey); letter-spacing: 0.5px;
  }
  .social { position: absolute; left: 1005px; top: 924px; display: flex; gap: 9px; }
  .social span { width: 20px; height: 20px; display: block; }
  .social .s1 { background: #3b5998; }
  .social .s2 { background: #2aa3e0; }
  .social .s3 { background: #1f77b0; }
  .social .s4 { background: #b51d1d; }
</style>
</head>
<body>
  <header class="brand">
    <span class="brand-mark"></span>
    <div class="brand-name">Quarry Provision Partners</div>
  </header>

  <div class="utility-icons">
    <svg width="14" height="14" viewBox="0 0 14 14" aria-label="Home"><path d="M7 1 L13 7 H11 V13 H8 V9 H6 V13 H3 V7 H1 Z" fill="#f5a71c"/></svg>
    <svg width="22" height="15" viewBox="0 0 22 15" aria-label="Email"><rect x="1" y="1" width="20" height="13" fill="none" stroke="#f5a71c" stroke-width="1.4"/><path d="M1 1 L11 9 L21 1" fill="none" stroke="#f5a71c" stroke-width="1.4"/></svg>
  </div>
  <div class="search"></div>
  <svg class="search-icon" width="13" height="13" viewBox="0 0 13 13" aria-label="Search"><circle cx="5.5" cy="5.5" r="4" fill="none" stroke="#1a1a1a" stroke-width="1.6"/><line x1="8.5" y1="8.5" x2="12" y2="12" stroke="#1a1a1a" stroke-width="1.8"/></svg>

  <section class="hero">
    <ul class="service-nav">
      <li class="active">Procurement Services</li>
      <li>Strategic Sourcing Services</li>
      <li>Lead Time Reduction Services</li>
      <li>Inventory Optimisation Services</li>
      <li>Critical Spare Parts Audit</li>
      <li>Suppy Chain Health Check</li>
    </ul>
    <div class="hero-photo" role="img" aria-label="Photo of heavy mining cutting machinery underground"></div>
  </section>

  <main class="content">
    <div class="page-head">
      <h1 class="page-title">PROCUREMENT SERVICES</h1>
      <div class="breadcrumb">Home | Procurement Services</div>
    </div>
    <div class="page-body">
      <div class="side-photo" role="img" aria-label="Photo of a businessman in a dark suit offering a handshake"></div>
      <div class="copy">
        <p>Praesent integer leo orci aliquam, nibh a. Diam nobis eget, erat natoque integer fringilla viverra. orem ipsum dolor sit amet, ligula nulla pretium, rhoncus tempor placerat fermentum, enim integer ad vestibulum volutpat. isl turpis est, vel elit, congue wisi enim nunc ultricies sit, magna tincidunt.Maecenas aliquam maecenas ligula nostra, accumsan taciti.tiam molestie mauris ligula eget laoreet, vehicula eleifend.</p>
        <p>Repellat orci eget erat et, sem cum, ultricies sollicitudin amet eleifend dolor nullam erat, malesuada est leo ac. Varius natoque turpis elementum est. cenas ligula nostra, accumsan taciti. Duis montes, tellus lobortis lacus amet arcu et. In vitae vel, wisi at, id praesent libero faucibus porta egestas, quisque praesent ipsum fermentum placerat tempor. Curabitur auctor, erat mollis sed fusce, turpis vivamus a dictumst congue magnis. Aliquam amet ullamcorper dignissim molestie, gravida mollis. Tortor vitae tortor eros wisi facilisis.</p>
        <p>Consectetuer arcu ipsum ornare pellentesque, feugiat at. Aptent morbi nibh mauris a, tortor eu vel vel suscipit. Donec quam, erat ut vel cursus. Praesent integer leo orci aliquam, nibh a. Diam nobis eget, erat natoque integer fringilla viverra. Lorem ipsum dolor sit amet, ligula nulla pretium,</p>
        <p>Rhoncus tempor placerat fermentum, enim integer ad vestibulum volutpat. Nisl turpis est, vel elit, congue wisi enim nunc ultricies sit, magna tincidunt. Maecenas aliquam maecenas ligula nostra, accumsan taciti.</p>
      </div>
    </div>
    <nav class="site-footer">Home |&nbsp; About Us |&nbsp;&nbsp; Contact Us &nbsp;&nbsp;| Terms &amp; Conditions &nbsp;&nbsp;|&nbsp;&nbsp; Site Map</nav>
  </main>

  <div class="copyright">Copyright 2015 Quarry Provision Partners. All Rights Reserved.</div>
  <div class="social" aria-label="Social links">
    <span class="s1"></span><span class="s2"></span><span class="s3"></span><span class="s4"></span>
  </div>
</body>
</html>
```